Patient Fact sheets for medical conditions and treatments

Hi,

I need a new design for my patient fact sheets. I am moving from my current clinic and I am looking from a new look.

I have attached
1. a current Fact sheet
2. New home page to the website
3. New Logo.

They need to be single page and easily readable for patients.

The will be in both PDF and print form in the future.

Target Market(s)

Patients with chronic pain age 40+

Font styles to use
Serif

Requirements
Must have
• My logo, should be inline with design elements on the Front page provided.

Please use the same font as the Logo

```html
<!DOCTYPE html>
<html lang="en">
<head>
<meta charset="utf-8">
<title>PRP Therapy Patient Fact Sheet</title>
<link rel="stylesheet" href="https://fonts.googleapis.com/css2?family=Mulish:ital,wght@0,400;0,600;0,700;1,400&family=Roboto+Condensed:wght@700&display=swap">
<style>
:root{
  --navy:#0e1640;
  --teal:#00a9bd;
  --teal-text:#13b3c4;
  --ink:#1a1f3a;
  --paper:#ffffff;
  --backdrop:#eceeef;
}
*{margin:0;padding:0;box-sizing:border-box}
html,body{width:1200px;height:1200px;overflow:hidden;background:var(--backdrop)}
.sheet{
  position:absolute;left:187px;top:20px;width:1007px;height:1413px;
  transform:scale(.8209);transform-origin:0 0;
  background:var(--paper);font-family:'Mulish',sans-serif;color:var(--ink);
  box-shadow:0 4px 18px rgba(0,0,0,.12);overflow:hidden;
}
.shapes{position:absolute;inset:0}
.abs{position:absolute}
.fact-label{left:35px;top:306px;font-weight:600;font-size:40px;color:#fff;letter-spacing:1px}
.clinic-name{left:520px;top:60px;width:360px;font-family:'Mulish',sans-serif;font-weight:600;font-size:24px;line-height:30px;color:var(--navy);text-align:right}
.title{left:455px;top:166px;font-family:'Roboto Condensed',sans-serif;font-weight:700;font-size:41px;line-height:37px;color:var(--teal-text)}
.title-rule{left:466px;top:263px;width:65px;height:3px;background:#fff}
.section-head{font-weight:600;font-size:19.5px;letter-spacing:.3px;color:var(--navy);text-transform:uppercase}
.intro-head{left:477px;top:292px;color:var(--teal-text);font-size:18.5px}
.intro-text{left:470px;top:332px;width:490px;font-size:14.4px;line-height:17.8px;color:#fff;text-align:center}
.body{font-size:14.6px;line-height:17.9px}
.work-head{left:35px;top:465px}
.work-text{left:36px;top:508px;width:448px}
.work-text p+p{margin-top:18px}
.role-head{left:526px;top:574px}
.role-text{left:527px;top:616px;width:440px}
.bullets{list-style:none;margin-top:18px}
.bullets li{position:relative;padding-left:17px;margin-bottom:6px}
.bullets li::before{content:"";position:absolute;left:1px;top:6px;width:7px;height:7px;border-radius:50%;background:var(--teal)}
.treat-band{left:0;top:912px;width:1007px;height:290px;background:var(--teal)}
.treat-head{left:37px;top:940px}
.treat-sub{left:35px;top:981px;font-weight:700;font-size:14.8px;color:#fff}
.treat-list{top:1005px;list-style:none;font-size:14.8px;line-height:23px;color:#fff}
.treat-list li{position:relative;padding-left:23px}
.treat-list li::before{content:"";position:absolute;left:3px;top:8px;width:8px;height:8px;border-radius:50%;background:var(--navy)}
.list-a{left:36px}
.list-b{left:346px}
.list-divider{left:305px;top:1010px;width:1.5px;height:102px;background:var(--navy)}
.treat-note{left:37px;top:1132px;width:420px;font-size:14.8px;line-height:18px;color:#fff}
.results-head{left:527px;top:943px}
.results-text{left:527px;top:986px;width:448px;font-size:14.6px;line-height:17.9px;color:#fff}
.disclaimer-head{left:35px;top:1216px;font-weight:700;font-size:12.5px;color:var(--navy)}
.disclaimer{left:36px;top:1238px;width:940px;font-size:10.4px;line-height:14px;color:var(--ink)}
.info-head{left:35px;top:1330px;font-weight:600;font-size:16.5px;color:var(--teal-text);letter-spacing:.3px}
.web{left:36px;top:1360px;display:flex;align-items:center;gap:10px;font-weight:700;font-size:21px;color:#fff}
.address{left:420px;top:1334px;font-size:14.6px;line-height:19.5px;color:#fff;display:flex;gap:8px}
.foot-divider{left:737px;top:1336px;width:1px;height:60px;background:#fff}
.contact{left:786px;top:1332px;font-size:14.6px;color:#fff;list-style:none}
.contact li{display:flex;align-items:center;gap:8px;height:25px}
.icon{width:15px;height:15px;flex:none}
</style>
</head>
<body>
<main class="sheet">
  <svg class="shapes" width="1007" height="1413" viewBox="0 0 1007 1413">
    <defs>
      <linearGradient id="photoTone" x1="0" y1="0" x2="1" y2="1">
        <stop offset="0" stop-color="#eef0f0"/>
        <stop offset=".55" stop-color="#d6d9da"/>
        <stop offset="1" stop-color="#c4c8c9"/>
      </linearGradient>
    </defs>
    <polygon role="img" aria-label="Photo of a gloved hand holding two blood sample tubes with separated yellow plasma" points="0,0 365,0 470,421 0,421" fill="url(#photoTone)"/>
    <polygon points="0,421 472,421 516,505 1007,505 1007,515 508,515 466,438 0,438" fill="var(--teal)"/>
    <polygon points="341,134 1007,134 1007,505 516,505" fill="var(--navy)"/>
    <polygon points="341,1313 1007,1313 1007,1413 390,1413" fill="var(--navy)"/>
    <polygon points="335,1303 1007,1303 1007,1310 339,1310" fill="var(--teal)"/>
    <polygon points="0,1359 355,1359 377,1392 0,1392" fill="var(--teal)"/>
  </svg>

  <div class="abs fact-label">FACT SHEET</div>
  <div class="abs clinic-name">Dr Ava Linton Pain Care</div>

  <h1 class="abs title">PLATELET RICH PLASMA (PRP)<br>THERAPY</h1>
  <div class="abs title-rule"></div>
  <h2 class="abs section-head intro-head">What is PRP?</h2>
  <p class="abs intro-text">Platelet-Rich Plasma (PRP) is concentrated platelets and white blood cells derived from your own blood. Platelet Rich Plasma Injection Therapy (PRP therapy), is a growing treatment approach for soft tissue injuries including tendon, muscle and ligaments. It is also showing good results for mild to moderate osteoarthritis. While this approach has been used overseas for many years, it's fairly new to Australia in the treatment of musculoskeletal and orthopaedic conditions.</p>

  <h2 class="abs section-head work-head">How does PRP work?</h2>
  <div class="abs body work-text">
    <p>Some tissues in the body have a poor blood supply or respond poorly to excessive load, ultimately failing to heal naturally. While some of our primary treatment such as physiotherapy, massage, biomechanical correction and other forms of treatment are used to treat these soft tissue injuries, sometimes the body fails to respond.</p>
    <p>PRP therapy utilises the healing properties in blood to allow a healing reaction to occur in a tissue that's not healing on its own. Our blood has small granules called 'platelets', which contain special growth factors that when released, allow stem cells in the particular tissue to 'switch' on and cause new tissue to be created and heal the injured area. HOW DOES PRP WORK? Take the example of achilles tendinopathy. If the achilles is painful, thickened and not responding to rehabilitation, then the sports physician will inject the PRP into the achilles which will cause the tendon cells (tenocytes/ fibroblasts) to create new achilles collagen to strengthen the achilles. White blood cells also enter the area to mop up any achilles tissue that may have been damaged due to the ongoing pain and thickening in the area.</p>
  </div>

  <h2 class="abs section-head role-head">Role of platelets &amp; growth factors</h2>
  <div class="abs body role-text">
    <p>PRP contains highly concentrated platelets. Platelets have been identified to secrete growth factors, which are known to play a role in:</p>
    <ul class="bullets">
      <li>Increasing tissue vascularity and increasing the rate of epithelial tissue production <em>(wound healing)</em></li>
      <li>Attracting other cells that fight infection</li>
      <li>Acting as a seal during closures</li>
      <li>Providing an immediate surgical hemostatic agent <em>(reduction of bleeding)</em></li>
      <li>Osteogenesis <em>(bone regeneration and repair)</em></li>
    </ul>
  </div>

  <section class="abs treat-band"></section>
  <h2 class="abs section-head treat-head">What can PRP treat?</h2>
  <div class="abs treat-sub">PRP therapy can be used for:</div>
  <ul class="abs treat-list list-a">
    <li>Orthopedic surgery</li>
    <li>Cardiac surgery</li>
    <li>Plastic and cosmetic surgery</li>
    <li>Ear, nose, throat (ent) surgery</li>
    <li>Oral maxillofacial surgery</li>
  </ul>
  <div class="abs list-divider"></div>
  <ul class="abs treat-list list-b">
    <li>Neurosurgery</li>
    <li>Vascular surgery</li>
    <li>Wound healing</li>
    <li>Burn care</li>
  </ul>
  <p class="abs treat-note">Ask your doctor whether plateletrich plasma is appropriate for your surgical procedure</p>

  <h2 class="abs section-head results-head">What are the expected results of PRP?</h2>
  <p class="abs results-text">Because the goal of PRP therapy is to resolve pain through healing, it could prove to have lasting results. Initial improvement may be seen within a few weeks, gradually increasing as the healing progresses. Research studies and clinical practice have shown PRP therapy to be very effective at relieving pain and returning patients to their normal lives. The need for surgery can also be greatly reduced by treating injured tissues before the damage progresses and the condition is irreversible.</p>

  <h3 class="abs disclaimer-head">DISCLAIMER</h3>
  <p class="abs disclaimer">Please note the contents contained in this Patient Fact Sheet are not intended as a substitute for your own independent health professional's advice, diagnosis or treatment. At Harbour Pain Group, we assess every patient's condition individually. As leaders in pain intervention, we aim to provide advanced, innovative, and evidence-based treatments tailored to suit each patient. As such, recommended treatments and their outcomes will vary from patient to patient. If you would like to find out whether our treatments are suitable for your specific condition, please speak to one of our doctors at the time of your consultation.</p>

  <div class="abs info-head">FOR MORE INFORMATION</div>
  <div class="abs web">
    <svg class="icon" viewBox="0 0 16 16" aria-hidden="true"><circle cx="8" cy="8" r="7" fill="var(--navy)"/><path d="M1 8h14M8 1c-3 3-3 11 0 14M8 1c3 3 3 11 0 14" stroke="#fff" stroke-width="1" fill="none"/></svg>
    <span>harbourpain.com.au</span>
  </div>

  <div class="abs address">
    <svg class="icon" viewBox="0 0 16 16" aria-hidden="true"><path d="M8 1a5 5 0 0 0-5 5c0 4 5 9 5 9s5-5 5-9a5 5 0 0 0-5-5z" fill="var(--teal)"/><circle cx="8" cy="6" r="2" fill="var(--navy)"/></svg>
    <div>Harbour Pain Group<br>Ridge House, Ground Floor<br>48 Kellett Road, Ashby VIC 3170</div>
  </div>
  <div class="abs foot-divider"></div>
  <ul class="abs contact">
    <li><svg class="icon" viewBox="0 0 16 16" aria-hidden="true"><circle cx="8" cy="8" r="8" fill="var(--teal)"/><path d="M5 4l2 0 1 2.5-1.2 1a5 5 0 0 0 2.7 2.7l1-1.2L13 10v2c-4 .5-8.5-4-8-8z" fill="var(--navy)"/></svg>03 9000 4821</li>
    <li><svg class="icon" viewBox="0 0 16 16" aria-hidden="true"><rect x="2" y="6" width="12" height="9" fill="var(--teal)"/><rect x="4" y="1" width="8" height="5" fill="none" stroke="var(--teal)" stroke-width="1.5"/><rect x="4" y="9" width="8" height="1.5" fill="var(--navy)"/></svg>03 9000 4822</li>
    <li><svg class="icon" viewBox="0 0 16 16" aria-hidden="true"><rect x="1" y="3" width="14" height="10" fill="var(--teal)"/><path d="M1 3l7 6 7-6" stroke="var(--navy)" stroke-width="1.4" fill="none"/></svg>info@harbourpain.com.au</li>
  </ul>
</main>
</body>
</html>
```